Redesign of Bright Harbor Entertainment Card

I already have my logo and font design for my company name. I am looking to come up with a Unique way of having it on my business card. Just looking for a really hip, and professional business card while still using my logo design.

I have also enclosed the front and back of the card so you can see what I have now. Looking for something different.

Thank you!

Target Market(s)

Young to middle aged brides and grooms

Industry/Entity Type

Business

Requirements
Should not have
• Cheese

```html
<!DOCTYPE html>
<html lang="en">
<head>
<meta charset="utf-8">
<title>Bright Harbor Entertainment – Business Card</title>
<link rel="stylesheet" href="https://fonts.googleapis.com/css2?family=Arimo:wght@400;700&display=swap">
<style>
  :root {
    --stage: #333333;
    --night: #03070f;
    --deep-blue: #0a2544;
    --harbor-blue: #0d4a70;
    --teal-wash: #11587f;
    --accent-blue: #29a3e0;
    --flare: #f2f8ff;
  }
  html, body {
    margin: 0;
    padding: 0;
    width: 1200px;
    height: 900px;
    overflow: hidden;
    background: var(--stage);
  }
  .canvas {
    position: relative;
    width: 1200px;
    height: 900px;
  }
  .card {
    position: absolute;
    left: 78px;
    top: 153px;
    width: 1044px;
    height: 593px;
    overflow: hidden;
  }
  .card-backdrop,
  .brand {
    position: absolute;
    left: 0;
    top: 0;
    width: 1044px;
    height: 593px;
    display: block;
  }
  .brand-name {
    font-family: "Arimo", Arial, sans-serif;
    font-weight: 700;
    fill: var(--accent-blue);
  }
  .brand-tagline {
    font-family: "Arimo", Arial, sans-serif;
    font-weight: 400;
    fill: var(--accent-blue);
  }
  .brand-rule {
    stroke: var(--accent-blue);
    stroke-width: 4;
  }
  .brand-dot {
    fill: none;
    stroke: var(--accent-blue);
    stroke-width: 5;
  }
</style>
</head>
<body>
<main class="canvas">
  <section class="card">
    <svg class="card-backdrop" viewBox="0 0 1044 593" role="img"
         aria-label="Grunge blue brush-stroke texture with fine light streaks and a bright stage light flare in the top right corner">
      <defs>
        <linearGradient id="backdrop-tone" x1="0" y1="0.2" x2="1" y2="0.8">
          <stop offset="0" stop-color="var(--deep-blue)"/>
          <stop offset="0.5" stop-color="var(--deep-blue)"/>
          <stop offset="1" stop-color="var(--teal-wash)"/>
        </linearGradient>
        <radialGradient id="dark-stroke" cx="0.5" cy="0.5" r="0.5">
          <stop offset="0" stop-color="var(--night)" stop-opacity="0.85"/>
          <stop offset="1" stop-color="var(--night)" stop-opacity="0"/>
        </radialGradient>
        <radialGradient id="light-wash" cx="0.5" cy="0.5" r="0.5">
          <stop offset="0" stop-color="var(--harbor-blue)" stop-opacity="0.9"/>
          <stop offset="1" stop-color="var(--harbor-blue)" stop-opacity="0"/>
        </radialGradient>
        <radialGradient id="stage-flare" cx="0.5" cy="0.5" r="0.5">
          <stop offset="0" stop-color="var(--flare)" stop-opacity="1"/>
          <stop offset="0.15" stop-color="#bfe2fb" stop-opacity="0.75"/>
          <stop offset="0.45" stop-color="#5fb0e3" stop-opacity="0.25"/>
          <stop offset="1" stop-color="#5fb0e3" stop-opacity="0"/>
        </radialGradient>
      </defs>
      <rect width="1044" height="593" fill="url(#backdrop-tone)"/>
      <ellipse cx="360" cy="260" rx="520" ry="150" transform="rotate(28 360 260)" fill="url(#dark-stroke)"/>
      <ellipse cx="200" cy="520" rx="300" ry="120" fill="url(#dark-stroke)"/>
      <ellipse cx="860" cy="470" rx="300" ry="180" fill="url(#light-wash)"/>
      <ellipse cx="160" cy="120" rx="220" ry="110" fill="url(#light-wash)" opacity="0.5"/>
      <circle cx="1002" cy="87" r="160" fill="url(#stage-flare)"/>
    </svg>

    <svg class="brand" viewBox="0 0 1044 593">
      <circle class="brand-dot" cx="245" cy="319" r="104"/>
      <text class="brand-name" x="367" y="302" font-size="116"
            textLength="515" lengthAdjust="spacingAndGlyphs">BRIGHT</text>
      <line class="brand-rule" x1="367" y1="317" x2="882" y2="317"/>
      <text class="brand-name" x="367" y="399" font-size="82"
            textLength="515" lengthAdjust="spacing">HARBOR</text>
      <text class="brand-tagline" x="367" y="430" font-size="20"
            textLength="515" lengthAdjust="spacing">ENTERTAINMENT &amp; EVENT PROFESSIONALS</text>
    </svg>
  </section>
</main>
</body>
</html>
```